Pharmacy ad

need 2 pharmacy ads for the phone book. one for Birchfield Pharmacy and one for Corvane Rx Pharmacy. Dimensions for ad is 4.75in x 4.667 in. please see attached examples of ad uploaded as well logos of each pharmacy

```html
<!DOCTYPE html>
<html lang="en">
<head>
<meta charset="utf-8">
<title>Birchfield Pharmacy – Directory Ad</title>
<link rel="stylesheet" href="https://fonts.googleapis.com/css2?family=Montserrat:wght@300;400;700;800&family=Open+Sans:ital,wght@1,600&display=swap">
<style>
  :root {
    --navy: #1c1a42;
    --sky-band: #86c9e4;
    --leaf-light: #cde3a3;
    --tagline: #7cb342;
    --white: #ffffff;
  }
  * { box-sizing: border-box; margin: 0; padding: 0; }
  html, body { width: 1200px; height: 1180px; overflow: hidden; background: var(--white); }
  .ad {
    position: relative; width: 1200px; height: 1180px; overflow: hidden;
    font-family: "Montserrat", Arial, sans-serif; color: var(--navy);
  }
  .backdrop { position: absolute; inset: 0; }
  .abs { position: absolute; }

  .offer { left: 40px; width: 500px; text-align: center; line-height: 1; }
  .offer-senior { top: 52px; }
  .offer-student { top: 372px; left: 50px; }
  .offer .pct { font-weight: 800; font-size: 92px; letter-spacing: -3px; display: block; }
  .offer .light { font-weight: 300; font-size: 42px; display: block; line-height: 1.0; }
  .offer .strong { font-weight: 800; font-size: 40px; display: block; line-height: 1.08; }
  .divider-dots {
    left: 112px; top: 338px; width: 348px; height: 8px;
    background-image: radial-gradient(circle, var(--navy) 2.6px, transparent 3px);
    background-size: 15.5px 8px;
  }

  .brand { left: 610px; top: 329px; width: 594px; text-align: center; }
  .brand-name { font-weight: 800; font-size: 78px; line-height: 90px; color: var(--navy); }
  .brand-tagline { margin-top: 22px; font-family: "Open Sans", Arial, sans-serif; font-style: italic; font-weight: 600; font-size: 29px; color: var(--tagline); }

  .services { top: 606px; font-size: 24px; font-weight: 400; line-height: 1.2; list-style: none; }
  .services li { position: relative; padding-left: 18px; margin-bottom: 14px; }
  .services li::before { content: "•"; position: absolute; left: 0; font-size: 18px; top: 2px; }
  .services-a { left: 56px; width: 290px; }
  .services-b { left: 358px; width: 260px; }
  .services-b li:nth-child(2) { margin-top: 6px; }
  .services-b li { margin-bottom: 22px; }

  .payments { left: 786px; top: 677px; width: 370px; }
  .payments .row { display: flex; justify-content: center; gap: 30px; margin-bottom: 18px; }
  .pay-chip {
    background: var(--white); height: 66px; width: 106px;
    display: flex; align-items: center; justify-content: center;
    font-weight: 700; font-size: 17px; color: var(--navy);
  }
  .pay-chip.wide { width: 246px; height: 50px; }

  .rule { left: 59px; top: 855px; width: 697px; height: 4px; background: var(--navy); }

  .hours { left: 57px; top: 877px; font-weight: 800; font-size: 35px; line-height: 48px; }
  .hours .note { font-weight: 400; font-size: 25px; }

  .location { font-size: 23px; line-height: 1.4; }
  .location .line { display: flex; align-items: flex-start; gap: 20px; }
  .location strong { font-weight: 800; }
  .location .sub { font-weight: 400; font-size: 20px; padding-left: 46px; }
  .location svg { flex: none; margin-top: 4px; }
  .loc-main { left: 62px; top: 1044px; }
  .loc-quay { left: 622px; top: 1044px; }

  .social { left: 994px; top: 1020px; width: 170px; text-align: center; }
  .social .label { font-size: 24px; font-weight: 400; }
  .social .name { margin-top: 10px; display: flex; flex-direction: column; align-items: center; gap: 4px; font-weight: 700; font-size: 20px; }
  .social .dot { width: 56px; height: 56px; border-radius: 50%; background: var(--navy); }
</style>
</head>
<body>
<main class="ad">
  <svg class="backdrop" width="1200" height="1180" viewBox="0 0 1200 1180" aria-hidden="true">
    <defs>
      <linearGradient id="sky" x1="0" y1="0" x2="1" y2="1">
        <stop offset="0" stop-color="#a9dcef"/>
        <stop offset="0.5" stop-color="#86c8e3"/>
        <stop offset="1" stop-color="#9fd4ea"/>
      </linearGradient>
      <linearGradient id="leaf" x1="0" y1="0" x2="1" y2="1">
        <stop offset="0" stop-color="#8fc356"/>
        <stop offset="0.6" stop-color="#b3d67e"/>
        <stop offset="1" stop-color="#d4e8ad"/>
      </linearGradient>
      <radialGradient id="haze" cx="0.35" cy="0.45" r="0.6">
        <stop offset="0" stop-color="#f4fafd"/>
        <stop offset="0.7" stop-color="#dcedf5"/>
        <stop offset="1" stop-color="#c3e0ee"/>
      </radialGradient>
      <clipPath id="lens"><circle cx="1242" cy="330" r="670"/></clipPath>
    </defs>
    <rect width="1200" height="1180" fill="url(#sky)"/>
    <rect y="575" width="1200" height="605" fill="url(#leaf)"/>
    <circle cx="1242" cy="330" r="670" fill="url(#haze)" role="img" aria-label="Soft blurred pharmacy shelf backdrop"/>
    <rect x="560" y="655" width="640" height="190" fill="var(--sky-band)" clip-path="url(#lens)"/>
  </svg>

  <section class="abs offer offer-senior">
    <span class="pct">10%</span>
    <span class="light">SENIOR CITIZEN<br>DISCOUNT</span>
    <span class="strong">FOR PATIENTS 60<br>YEARS AND OVER</span>
  </section>
  <div class="abs divider-dots"></div>
  <section class="abs offer offer-student">
    <span class="pct">10%</span>
    <span class="light">STUDENT DISCOUNT</span>
    <span class="strong">WITH VALID ID CARD</span>
  </section>

  <section class="abs brand">
    <h1 class="brand-name">BIRCHFIELD<br>PHARMACY</h1>
    <p class="brand-tagline">We Care About Your Health</p>
  </section>

  <ul class="abs services services-a">
    <li>Certified Pharmacists</li>
    <li>Affordable prices</li>
    <li>Brand and<br>Generic Medicines</li>
    <li>Blood Pressure and Glucose checks</li>
  </ul>
  <ul class="abs services services-b">
    <li>Personal care and Beauty Products</li>
    <li>Injectables</li>
    <li>Special Orders</li>
    <li>Delivery service</li>
  </ul>

  <section class="abs payments" aria-label="Accepted payments and insurers">
    <div class="row">
      <div class="pay-chip">Paycrest</div>
      <div class="pay-chip">Orbicard</div>
      <div class="pay-chip">Selvora</div>
    </div>
    <div class="row">
      <div class="pay-chip wide">Tradewind Insurances</div>
    </div>
  </section>

  <div class="abs rule"></div>

  <section class="abs hours">
    <p>MONDAY – FRIDAY 10AM TO 6PM</p>
    <p>SATURDAY 10AM TO 5PM</p>
    <p>SUNDAY 10AM TO 2PM <span class="note">(MARLOW STREET BRANCH)</span></p>
  </section>

  <section class="abs location loc-main">
    <div class="line">
      <svg width="24" height="30" viewBox="0 0 24 30"><path d="M12 0C5.4 0 0 5.3 0 11.8 0 20 12 30 12 30s12-10 12-18.2C24 5.3 18.6 0 12 0z" fill="var(--navy)"/><circle cx="12" cy="11.5" r="4.5" fill="var(--leaf-light)"/></svg>
      <strong>27 Marlow Street, Kestrelton</strong>
    </div>
    <div class="sub">(opposite Greyfield Chapel)</div>
    <div class="line">
      <svg width="28" height="24" viewBox="0 0 28 24"><path d="M2 9c0-5 24-5 24 0v3h-6V9c-3-1-9-1-12 0v3H2z" fill="var(--navy)"/><path d="M6 13h16l3 10H3z" fill="var(--navy)"/><circle cx="14" cy="18" r="2.5" fill="var(--leaf-light)"/></svg>
      <strong>555-0174</strong>
    </div>
  </section>

  <section class="abs location loc-quay">
    <div class="line">
      <svg width="24" height="30" viewBox="0 0 24 30"><path d="M12 0C5.4 0 0 5.3 0 11.8 0 20 12 30 12 30s12-10 12-18.2C24 5.3 18.6 0 12 0z" fill="var(--navy)"/><circle cx="12" cy="11.5" r="4.5" fill="var(--leaf-light)"/></svg>
      <strong>Harbour Quay, Food Court,<br>Kestrelton</strong>
    </div>
    <div class="line">
      <svg width="28" height="24" viewBox="0 0 28 24"><path d="M2 9c0-5 24-5 24 0v3h-6V9c-3-1-9-1-12 0v3H2z" fill="var(--navy)"/><path d="M6 13h16l3 10H3z" fill="var(--navy)"/><circle cx="14" cy="18" r="2.5" fill="var(--leaf-light)"/></svg>
      <strong>555- 0177</strong>
    </div>
  </section>

  <section class="abs social">
    <p class="label">Visit us on</p>
    <div class="name"><span class="dot"></span>Friendgrid</div>
  </section>
</main>
</body>
</html>
```